Velvor IT Services Business Card

Velvor IT Services are a Perth based IT Services company. We would like to incorporate our company logo (attached) and stick with the blue that is in that design. I would like a clean look design that isn't too busy, yet creates a lasting image that is instantly recognisable in the recipients mind.

Target Market(s)

The target audience is small/medium business owners.

Industry/Entity Type

Business

Font styles to use
Serif
Sans Serif

Colors

Designer to choose colors to be used in the design.

Requirements
Must have
• The design should include:
Business name: Velvor IT Services
Directors Name: Marcus Dredge
Phone Number: 0483 906 452
Email: support@velvorit.com.au
Website: www.velvorit.com.au

```html
<!DOCTYPE html>
<html lang="en">
<head>
<meta charset="utf-8">
<title>Velvor IT Services – Business Card</title>
<link rel="stylesheet" href="https://fonts.googleapis.com/css2?family=Questrial&display=swap">
<style>
  :root {
    --stage: #e4e2df;
    --card-white: #f3f3f3;
    --card-black: #0b0b0b;
    --brand-blue: #1e8fe0;
    --logo-blue: #1a63c9;
    --text-light: #e6e6e6;
    --shadow: rgba(0, 0, 0, 0.18);
  }
  * { box-sizing: border-box; margin: 0; padding: 0; }
  html, body {
    width: 1200px;
    height: 900px;
    overflow: hidden;
    background: var(--stage);
    font-family: "Questrial", sans-serif;
  }
  .canvas {
    position: relative;
    width: 1200px;
    height: 900px;
  }
  .card {
    position: absolute;
    left: 285px;
    width: 630px;
    height: 360px;
    overflow: hidden;
    box-shadow: 0 6px 18px var(--shadow);
  }
  .card--front { top: 60px; background: var(--card-white); }
  .card--back { top: 480px; background: var(--card-black); }

  .brand {
    position: absolute;
    display: flex;
    align-items: center;
    gap: 12px;
    color: var(--logo-blue);
    white-space: nowrap;
  }
  .brand__mark {
    display: block;
    background: var(--brand-blue);
  }
  .card--front .brand {
    left: 50%;
    top: 50%;
    transform: translate(-50%, -50%);
    font-size: 34px;
  }
  .card--front .brand__mark { width: 26px; height: 26px; }

  .back__panel {
    position: absolute;
    left: 0;
    top: 0;
    width: 252px;
    height: 360px;
    background: var(--card-white);
  }
  .card--back .brand {
    left: 126px;
    top: 150px;
    transform: translate(-50%, -50%);
    font-size: 19px;
    gap: 8px;
  }
  .card--back .brand__mark { width: 14px; height: 14px; }

  .name-band {
    position: absolute;
    left: 240px;
    top: 84px;
    width: 390px;
    height: 46px;
    background: var(--brand-blue);
    border-radius: 8px 0 0 8px;
    display: flex;
    align-items: center;
    padding-left: 42px;
  }
  .name-band__name {
    color: #ffffff;
    font-size: 24px;
    letter-spacing: 0.5px;
  }

  .contacts {
    position: absolute;
    left: 278px;
    top: 178px;
    list-style: none;
  }
  .contacts__item {
    display: flex;
    align-items: baseline;
    gap: 16px;
    height: 30px;
    color: var(--text-light);
    font-size: 17px;
    letter-spacing: 0.6px;
  }
  .contacts__label {
    width: 12px;
    color: var(--brand-blue);
    font-size: 13px;
    font-weight: 700;
  }
</style>
</head>
<body>
<main class="canvas">
  <section class="card card--front" aria-label="Business card front">
    <div class="brand">
      <span class="brand__mark" aria-hidden="true"></span>
      <span class="brand__name">Velvor IT Services</span>
    </div>
  </section>

  <section class="card card--back" aria-label="Business card back">
    <div class="back__panel">
      <div class="brand">
        <span class="brand__mark" aria-hidden="true"></span>
        <span class="brand__name">Velvor IT Services</span>
      </div>
    </div>
    <div class="name-band">
      <span class="name-band__name">Marcus Dredge</span>
    </div>
    <ul class="contacts">
      <li class="contacts__item"><span class="contacts__label">P</span><span>0483 906 452</span></li>
      <li class="contacts__item"><span class="contacts__label">E</span><span>support@velvorit.com.au</span></li>
      <li class="contacts__item"><span class="contacts__label">W</span><span>www.velvorit.com.au</span></li>
    </ul>
  </section>
</main>
</body>
</html>
```